Email PDF Guide for Brightlane

We are an online professional services website which helps start ups and small businesses gain access to the R&D tax incentive.

We want to educate businesses across multiple industries to understand what they need to do to access this tax incentive, with information relevant to their industry. We need a designer to pull together and design images and relevant visuals for a downloadable guide. Please note - we will provide all the content for this, your job is to pull this into a stylised guide, which is inviting to our audience and compliment the words with imagery.

We are looking to produce 12 guides in total but will start with one to confirm design and style. Then follow up with remaining 11 industries.

First industry: Technology and Software

To get a sense for what we do our site is: https://www.brightlane-example.com/

Very interested to hear what the community comes up with to create something visually engaging and relevant to our site and message.

Target Market(s)

Start up founders and entrepreneurs in technology industry. Average age 35.

Industry/Entity Type

Information Technology

Font styles to use
Other font styles liked:
• Proxima Nova

Requirements
Must have
• - Guide needs to be minimum of 8 pages, content currently totals 5 word pages.
• - The format needs to be editable on standard Google or Microsoft products then formatted into PDF, so we can make text changes at later dates (can discuss this criteria if difficult)
• - Font is Proxima Nova
• - Colours and gradients can be found here: http://tavelspring.examplehost.com/
• - Colour selection should be:
• * Main palette = #ff7c14 , #ffa800 , #fc4e78
• * Gray palette = #cccccc , #c1d1d9 , #f5f7f9 , #080808 , #2d3338 , #666666 , #6f7c82 , #999999
Nice to have
• Play with the title for best design format.
• Happy with one of the following options:
• - R&D in the Technology Industry
• - What you need to know about R&D in Technologu

```html
<!DOCTYPE html>
<html lang="en">
<head>
<meta charset="utf-8">
<title>R&amp;D in the Technology Industry – Brightlane Guide</title>
<link rel="stylesheet" href="https://fonts.googleapis.com/css2?family=Figtree:ital,wght@0,400;0,500;0,600;1,400&display=swap">
<style>
  :root{
    --orange:#f68b1f;
    --orange-deep:#ff7c14;
    --band:#f2f2f2;
    --canvas:#f4f4f4;
    --ink:#2d3338;
    --muted:#666666;
    --paper:#ffffff;
    --frame:#9a9a9a;
  }
  *{box-sizing:border-box;margin:0;padding:0}
  html,body{width:1200px;height:1000px;overflow:hidden;background:var(--canvas)}
  body{position:relative;font-family:"Figtree",Arial,sans-serif;color:var(--ink)}
  h1,h2{font-weight:400}
  .page{position:absolute;width:291px;height:412px;background:var(--paper);border:1px solid var(--frame);overflow:hidden}
  .p1{left:4px;top:46px}.p2{left:305px;top:46px}.p3{left:607px;top:46px}.p4{left:906px;top:46px}
  .p5{left:4px;top:467px}.p6{left:305px;top:467px}.p7{left:607px;top:467px}.p8{left:906px;top:467px}

  .footer-art{position:absolute;left:0;right:0;bottom:0;height:42px;
    background:linear-gradient(90deg,#fdf3ea 0%,#fbe2cb 35%,#fdeedf 60%,#fbdcbd 100%)}
  .cover-art{position:absolute;left:0;right:0;bottom:0;height:150px;
    background:linear-gradient(100deg,#fde3c8 0%,#f9b066 30%,#fbd6b0 55%,#fbc189 80%,#fbc893 100%)}
  .page-no{position:absolute;right:30px;bottom:4px;font-size:8px;color:var(--ink)}

  .brand-row{position:absolute;left:10px;top:26px;display:flex;align-items:center}
  .brand-mark{display:flex;align-items:center;gap:4px;font-size:12px;font-weight:600;color:var(--ink);width:55px}
  .brand-mark .sq{width:9px;height:9px;background:var(--orange)}
  .brand-product{font-size:13px;color:var(--muted)}
  .cover-title{position:absolute;left:0;right:0;top:92px;text-align:center;color:var(--orange)}
  .cover-title .big{display:block;font-size:32px;line-height:36px}
  .cover-title .sub{display:block;font-size:21px;line-height:26px}
  .cover-by{position:absolute;left:0;right:0;top:162px;text-align:center;font-size:8px;font-style:italic}

  .contents-title{position:absolute;left:18px;top:88px;font-size:19px;color:var(--orange)}
  .contents-list{position:absolute;left:18px;top:113px;list-style:none;font-size:9.3px;line-height:11.8px;color:var(--ink)}

  .band{position:absolute;left:0;width:290px;height:24px;background:var(--band);
    clip-path:polygon(0 0,100% 0,92% 100%,0 100%);padding-left:20px;
    font-size:13px;line-height:24px;color:var(--orange)}
  .band.tall{height:38px;line-height:17px;padding-top:3px}
  .body-text{position:absolute;left:20px;width:252px;font-size:7.4px;line-height:9.5px;color:var(--ink)}
  .body-text p{margin-bottom:9.5px}
  .body-text ul{list-style:none;margin-bottom:9.5px}
  .body-text li{padding-left:16px;position:relative}
  .body-text li::before{content:"•";position:absolute;left:0}

  .back-contact{position:absolute;left:0;right:0;top:143px;text-align:center;color:var(--orange);font-size:9.5px;line-height:12.5px}
  .back-art{position:absolute;left:0;right:0;bottom:0;height:150px;
    background:linear-gradient(100deg,#fce8d4 0%,#f9b874 30%,#fbd9b6 55%,#f9b066 80%,#fbc58e 100%)}
</style>
</head>
<body>

<section class="page p1">
  <div class="brand-row">
    <div class="brand-mark"><span class="sq"></span>Pemrixo</div>
    <div class="brand-product">Brightlane R&amp;D</div>
  </div>
  <h1 class="cover-title"><span class="big">R&amp;D</span><span class="sub">in the Technology Industry</span></h1>
  <p class="cover-by">By: Brightlane</p>
  <div class="cover-art" role="img" aria-label="Overlapping translucent orange and grey squares"></div>
</section>

<section class="page p2">
  <h2 class="contents-title">Content</h2>
  <ol class="contents-list">
    <li>1: Introduction</li>
    <li>2: Summary of R&amp;D Tax Incentive</li>
    <li>3: What is R&amp;D?</li>
    <li>4: Benefits of conducting R&amp;D activities</li>
    <li>5: Eligibility to claim the R&amp;D Tax Incentive</li>
    <li>6: Claiming the R&amp;D Tax Incentive in the Technology sector</li>
    <li>7: Registration of R&amp;D activities</li>
    <li>8: Applying for the R&amp;D Tax Incentive</li>
  </ol>
  <div class="footer-art" role="img" aria-label="Soft peach squares footer"></div>
</section>

<section class="page p3">
  <h2 class="band" style="top:28px">1: Introduction</h2>
  <div class="body-text" style="top:62px">
    <p>The technology industry is always evolving. Businesses and startups within the industry seek to innovate and take part in Research &amp; Development projects (R&amp;D) to stay ahead.</p>
    <p>If your tech company works on innovative projects, you may be eligible for a tax offset under the R&amp;D Tax Incentive.</p>
  </div>
  <h2 class="band" style="top:146px">2: Summary of R&amp;D Tax Incentive</h2>
  <div class="body-text" style="top:180px">
    <p>The Australian government supports innovation by encouraging local businesses to develop new or improved products and original solutions. This support is offered through the Research &amp; Development (R&amp;D) Tax Incentive, reducing the financial risk involved in undertaking R&amp;D activities. By reducing the risks and costs associated with conducting R&amp;D, the incentive seeks to boost productivity, innovation and economic growth for the nation.</p>
    <p>The R&amp;D Tax Incentive offers a targeted tax offset of up to a 45% refund of costs for eligible Research &amp; Development activities that benefit Australia.</p>
    <p>Many businesses in Australia are already completing eligible R&amp;D activities without realising. In fact, only 30% of eligible small businesses conducting R&amp;D currently claim this tax incentive. You don't need to be conducting experiments in a lab to qualify for R&amp;D incentives. If your business prides itself on innovation or is considering new developments, read on to find out more about how the R&amp;D Tax Incentive could provide cash back to your company.</p>
  </div>
  <div class="footer-art" role="img" aria-label="Soft peach squares footer"></div>
  <span class="page-no">1</span>
</section>

<section class="page p4">
  <h2 class="band" style="top:24px">3: What is R&amp;D?</h2>
  <div class="body-text" style="top:54px">
    <p>Research &amp; Development, or R&amp;D, involves conducting an experiment or trial to gain new knowledge. This new knowledge could be used to develop new or improved materials, products, devices, processes, software, or services. An experiment doesn't have to be scientific, all it means it that at the start of this process you're unaware of what the outcome will be and need to conduct further research, testing and trialling in order to overcome this uncertainty. The results seek to bridge the gap in knowledge that you started with.</p>
    <p>A wide range of businesses and industries conduct R&amp;D activities including (but not limited to):</p>
    <ul><li>Professional services</li><li>Manufacturing</li><li>Agriculture</li><li>Retail</li><li>Fashion</li><li>Science</li><li>Technology</li></ul>
  </div>
  <div class="footer-art" role="img" aria-label="Soft peach squares footer"></div>
  <span class="page-no">2</span>
</section>

<section class="page p5">
  <h2 class="band" style="top:18px">4: Benefits of conducting R&amp;D activities</h2>
  <div class="body-text" style="top:46px">
    <p>Research and Development helps to improve workforce skills and knowledge, venture capital opportunities, and technical proficiencies within a business. Innovation and cutting-edge solutions not only puts your company at the forefront of competition, it also supports the development of the Australian workforce and economy.</p>
    <p>Financial benefits of R&amp;D Tax Incentive</p>
    <p>Undertaking R&amp;D involves significant technical and financial risk. The R&amp;D Tax Incentive was introduced to encourage businesses in Australia to take on R&amp;D activities. Unlike a grant, you are not applying for funding or competing with other businesses for this financial incentive. Instead, the financial benefit is received in the way of tax offsets against expenses and is available to all eligible businesses.</p>
    <p>Small businesses (turnover below $20 million) can receive a 45% R&amp;D tax offset against expenses in a financial year. Larger companies (over $20 million aggregated turnover) can receive a 40% R&amp;D tax offset.</p>
    <p>Companies that have experienced a tax loss can also benefit from the R&amp;D Tax Incentive and could be eligible to offset 45cents for every dollar spent on R&amp;D activities.</p>
  </div>
  <div class="footer-art" role="img" aria-label="Soft peach squares footer"></div>
  <span class="page-no">3</span>
</section>

<section class="page p6">
  <h2 class="band" style="top:18px">5: Eligibility to claim the R&amp;D Tax Incentive</h2>
  <div class="body-text" style="top:46px">
    <p>More than 20,000 small businesses are currently eligible for the R&amp;D Tax Incentive, yet only 7,000 currently apply for this program.</p>
    <p>When you hear R&amp;D, you might be thinking of large corporations developing new products in laboratories. This is a common misconception, but almost every type of business conducts R&amp;D in one form of another, regardless of their size or industry.</p>
    <p>Your business is likely to be eligible if it is:</p>
    <ul><li>Incorporated as a company</li><li>A for-profit entity</li><li>Registered in Australia</li><li>Spent more than $20,000 on eligible R&amp;D expenses</li></ul>
    <p>However, you are not eligible to apply your business is:</p>
    <ul><li>An individual sole trader</li><li>A corporate limited partnership</li><li>An exempt entity (where your entire income is exempt from income tax).</li></ul>
    <p>Your business can only benefit from the program if your initiatives are considered eligible R&amp;D activities and meet the legal requirements. This is to ensure that companies do not take advantage of the program solely for the purpose of gaining additional income.</p>
  </div>
  <div class="footer-art" role="img" aria-label="Soft peach squares footer"></div>
  <span class="page-no">4</span>
</section>

<section class="page p7">
  <h2 class="band tall" style="top:18px">6: Claiming the R&amp;D Tax Incentive in the Technology sector</h2>
  <div class="body-text" style="top:60px">
    <p>When it comes to R&amp;D in the tech industry, there are some important factors to consider.</p>
    <p>R&amp;D for software and web/mobile applications</p>
    <p>R&amp;D in the technology industry often involves code development to improve or create new software that offers unique features.</p>
    <p>Unfortunately, it can be challenging to identify if code writing and development can qualify as eligible R&amp;D. This is because most of the activities for code development are similar and not considered unique or 'new knowledge'.</p>
    <p>Approximately 20% of the code for web applications and platforms are original. The remaining 80% is considered to be conventional and easily accessible by other developers. To justify that your code is new and innovative, it must enable a software and/or application to complete a complex feature. This feature could not be developed without first trialling because the step-by-step knowledge is not publicly known.</p>
    <p>Examples of complex features include (but are not limited to):</p>
    <p>• Image and video processing<br>This is complex because image and video processing requires processing of bigger data size as compared to text file</p>
    <p>• Analysing of data between dissimilar applications<br>There is complexity in translating a specific format into another</p>
    <p>• Utilisation of GPS data<br>This is complex because there is only a certain degree of accuracy when it comes to GPS data. Data integrity is also influenced by remoteness of</p>
  </div>
  <div class="footer-art" role="img" aria-label="Soft peach squares footer"></div>
  <span class="page-no">5</span>
</section>

<section class="page p8">
  <div class="back-contact">
    <p>Brightlane</p>
    <p>Email: support@brightlane-example.com</p>
    <p>Phone: 1800 555 019</p>
  </div>
  <div class="back-art" role="img" aria-label="Overlapping translucent orange and grey squares"></div>
</section>

</body>
</html>
```